New business stationairy

I need paper with header and footer and business cards.
I am a Ltd Company and my main field of expertise is QA/QC inspection in the Oil and Gas Industry. I will need all contact detail inserted and a footer with registration number and bank details etc

Business

```html
<!DOCTYPE html>
<html lang="en">
<head>
<meta charset="utf-8">
<title>Harrow Inspection Services Ltd – Stationery</title>
<link rel="stylesheet" href="https://fonts.googleapis.com/css2?family=EB+Garamond:wght@500&family=Roboto+Condensed:wght@400;500&display=swap">
<style>
  :root {
    --backdrop: #2f5ae0;
    --paper: #f7f7f7;
    --navy: #2b3f8c;
    --sky: #1f8fc9;
    --ink: #1f2a55;
    --ghost: #e6e6e6;
  }
  * { margin: 0; padding: 0; box-sizing: border-box; }
  html, body { width: 1200px; height: 987px; overflow: hidden; }
  body {
    background: var(--backdrop);
    position: relative;
    font-family: "Roboto Condensed", Arial, sans-serif;
  }
  .sheet, .card {
    position: absolute;
    background: var(--paper);
    overflow: hidden;
    box-shadow: 0 10px 30px rgba(0, 0, 40, .35);
  }
  .bands { position: absolute; inset: 0; width: 100%; height: 100%; }

  /* Letterhead */
  .letterhead { left: 90px; top: 120px; width: 530px; height: 750px; }
  .letterhead .brand { position: absolute; left: 40px; top: 70px; }
  .letterhead .watermark {
    position: absolute; left: 120px; top: 200px;
    width: 300px; height: 300px; border-radius: 50%;
    border: 14px solid var(--ghost);
  }
  .brand {
    display: flex; align-items: center; gap: 10px;
    font-family: "EB Garamond", Georgia, serif;
    font-weight: 500; color: var(--navy);
    line-height: 1.05;
  }
  .brand .dot { width: 22px; height: 22px; border-radius: 50%; background: var(--sky); flex: none; }
  .brand .name { font-size: 19px; border-left: 1px solid var(--navy); padding-left: 8px; }

  .footer-info {
    position: absolute; right: 34px; bottom: 112px;
    display: flex; gap: 18px; font-size: 10.5px; color: var(--ink);
  }
  .registry { color: var(--sky); line-height: 1.55; text-align: right; }
  .contact { list-style: none; line-height: 1.55; }
  .contact li { display: flex; align-items: center; gap: 6px; }
  .contact svg { width: 10px; height: 10px; fill: var(--sky); flex: none; }

  /* Business cards */
  .card { width: 420px; height: 240px; }
  .card-front { left: 700px; top: 560px; }
  .card-front .brand { position: absolute; left: 70px; top: 88px; }
  .card-front .brand .name { font-size: 21px; }
  .card-back { left: 700px; top: 230px; }
  .card-back .brand { position: absolute; left: 30px; top: 30px; }
  .card-back .brand .name { font-size: 17px; }
  .card-back .contact { position: absolute; left: 32px; top: 108px; font-size: 11px; color: var(--ink); }
  .holder { position: absolute; right: 22px; top: 40px; text-align: right; }
  .holder .person { color: #4fb3ea; font-size: 17px; font-weight: 500; }
  .holder .role { color: #fff; font-size: 10px; }
</style>
</head>
<body>

<section class="sheet letterhead" aria-label="Letterhead">
  <svg class="bands" viewBox="0 0 530 750" preserveAspectRatio="none" aria-hidden="true">
    <path fill="var(--navy)" d="M530 0 L530 30 C360 22 200 12 0 4 L0 0 Z"/>
    <path fill="var(--sky)" d="M530 36 L530 46 C400 40 260 36 150 42 C280 32 420 32 530 36 Z"/>
    <path fill="var(--navy)" d="M0 750 L0 700 C200 710 380 726 530 742 L530 750 Z"/>
    <path fill="var(--sky)" d="M0 692 L0 680 C160 684 330 698 450 718 C330 706 160 696 0 692 Z"/>
  </svg>
  <div class="watermark" aria-hidden="true"></div>
  <div class="brand">
    <span class="dot"></span>
    <span class="name">Harrow Inspection<br>Services Ltd</span>
  </div>
  <div class="footer-info">
    <div class="registry">
      Vat No. # 00000000<br>
      Bank No. # 1111111111<br>
      Reg. No. # 1122334455
    </div>
    <ul class="contact">
      <li><svg viewBox="0 0 10 10"><path d="M2 0 L4 2 L3 3.5 C4 5.5 4.5 6 6.5 7 L8 6 L10 8 L8.5 10 C4 9.5 .5 6 0 1.5 Z"/></svg>07700 900123</li>
      <li><svg viewBox="0 0 10 10"><path d="M0 2 H10 V8 H0 Z M0 2 L5 6 L10 2" /></svg>office@harrowinspect.co.uk</li>
      <li><svg viewBox="0 0 10 10"><path d="M5 0 C2.5 0 1 2 1 4 C1 6.5 5 10 5 10 C5 10 9 6.5 9 4 C9 2 7.5 0 5 0 Z"/></svg>12 Mill Lane Ashford<br>Dorset DT1 0ZZ</li>
    </ul>
  </div>
</section>

<section class="card card-back" aria-label="Business card, contact side">
  <svg class="bands" viewBox="0 0 420 240" preserveAspectRatio="none" aria-hidden="true">
    <path fill="var(--navy)" d="M420 0 L340 0 C300 70 320 150 200 240 L420 240 Z"/>
    <path fill="var(--sky)" d="M326 0 L334 0 C290 80 300 160 170 240 L150 240 C290 160 280 80 326 0 Z"/>
    <path fill="var(--sky)" d="M130 240 C200 210 260 180 290 130 C270 190 220 220 160 240 Z" opacity=".6"/>
  </svg>
  <div class="brand">
    <span class="dot"></span>
    <span class="name">Harrow Inspection<br>Services Ltd</span>
  </div>
  <ul class="contact">
    <li><svg viewBox="0 0 10 10"><path d="M2 0 L4 2 L3 3.5 C4 5.5 4.5 6 6.5 7 L8 6 L10 8 L8.5 10 C4 9.5 .5 6 0 1.5 Z"/></svg>07700 900123</li>
    <li><svg viewBox="0 0 10 10"><path d="M0 2 H10 V8 H0 Z"/></svg>office@harrowinspect.co.uk</li>
    <li><svg viewBox="0 0 10 10"><path d="M5 0 C2.5 0 1 2 1 4 C1 6.5 5 10 5 10 C5 10 9 6.5 9 4 C9 2 7.5 0 5 0 Z"/></svg>12 Mill Lane Ashford<br>Dorset DT1 0ZZ</li>
  </ul>
  <div class="holder">
    <div class="person">Sam Harrow</div>
    <div class="role">Owner</div>
  </div>
</section>

<section class="card card-front" aria-label="Business card, name side">
  <div class="brand">
    <span class="dot"></span>
    <span class="name">Harrow Inspection<br>Services Ltd</span>
  </div>
</section>

</body>
</html>
```